Stationery design for a financial consulting firm
K&R Ledger Partners
Stationery design for a financial consulting firm - Consulting
Creative Brief
Corporate
Yusuf K. Halabi يوسف خالد حلبي
Senior Financial Consultant - GM مستشار مالي اول - مدير عام
P.O Box 274816, Jeddah 21947 , KSA
Jeddah , KSA
yusuf.halabi@krledgerpartners.example
TQRW482 TQRW482
Dear Sir, I believe the word in Arabic for " مالي " was fine no need to change. Best regards, Yusuf Halabi
Thanks for the card design and i have noticed that draft # 38 is the most likely favorable one. Please make a change of the followings:- 1- address to read as follow:- P.O Box 81924 Jeddah 21688 KSA 2- The telephone number to read as +966-50711-2938 3- My first name in Arabic to read يوسف 4- مالي not مالى Best reagrds, Yusuf Halabi
kamranwali kamranwali
where is logo?

```html
<!DOCTYPE html>
<html lang="en">
<head>
<meta charset="utf-8">
<title>K&amp;R Ledger Partners — Business Card</title>
<link rel="stylesheet" href="https://fonts.googleapis.com/css2?family=Lato:wght@400;700;900&display=swap">
<style>
  :root {
    --page: #e9ebee;
    --card-dark: #1d1e21;
    --card-light: #ffffff;
    --accent: #3fa9f5;
    --accent-deep: #2b8fdc;
    --ink: #1d1e21;
    --text-light: #e8eaee;
    --text-muted: #b8bcc4;
  }
  * { margin: 0; padding: 0; box-sizing: border-box; }
  html, body { width: 1200px; height: 1000px; overflow: hidden; }
  body {
    background: var(--page);
    font-family: "Lato", Arial, sans-serif;
    position: relative;
  }
  .card {
    position: absolute;
    top: 170px;
    width: 380px;
    height: 660px;
    border-radius: 6px;
    overflow: hidden;
    box-shadow: 0 14px 34px rgba(0,0,0,.22);
  }
  .card-front { left: 190px; background: var(--card-dark); }
  .card-back  { left: 630px; background: var(--card-dark); }
  .card-shapes { position: absolute; inset: 0; }

  .brand {
    position: absolute;
    left: 0; right: 0;
    display: flex;
    flex-direction: column;
    align-items: center;
    text-align: center;
  }
  .brand-mark {
    width: 54px; height: 54px;
    background: var(--accent);
    margin-bottom: 12px;
  }
  .brand-name {
    font-weight: 900;
    font-size: 25px;
    line-height: 1.15;
    width: 240px;
  }
  .card-front .brand { top: 118px; }
  .card-front .brand-name { color: var(--ink); }
  .card-back .brand { top: 96px; }
  .card-back .brand-name { color: var(--text-light); }

  .email {
    position: absolute;
    top: 252px; left: 0; right: 0;
    text-align: center;
    font-size: 12.5px;
    font-weight: 700;
    color: var(--ink);
  }

  .name-banner {
    position: absolute;
    top: 288px; left: 0;
    width: 318px; height: 84px;
    background: var(--accent);
    border-radius: 0 42px 42px 0;
    padding: 14px 0 0 34px;
    color: #fff;
  }
  .person-name { font-size: 29px; font-weight: 900; letter-spacing: .2px; }
  .person-title { font-size: 15px; font-weight: 400; margin-top: 3px; }

  .contact-list {
    position: absolute;
    top: 470px; left: 34px;
    list-style: none;
    color: var(--text-light);
    font-size: 15px;
  }
  .contact-list li { display: flex; align-items: center; margin-bottom: 11px; }
  .contact-icon {
    width: 24px; height: 24px;
    border-radius: 50%;
    background: #3a3c41;
    margin-right: 14px;
    flex: none;
    display: flex; align-items: center; justify-content: center;
  }

  .signature {
    position: absolute;
    top: 330px; left: 90px;
    width: 200px; height: 64px;
    background: linear-gradient(180deg, rgba(232,234,238,.16), rgba(232,234,238,.06));
    border-radius: 4px;
  }
</style>
</head>
<body>

  <section class="card card-front" aria-label="Business card front">
    <svg class="card-shapes" viewBox="0 0 380 660" width="380" height="660" aria-hidden="true">
      <path d="M0 0 H380 V330 H0 Z" fill="var(--card-light)"/>
      <path d="M0 0 H92 Q50 10 34 60 L34 150 Q28 170 0 176 Z" fill="var(--accent)"/>
      <path d="M380 660 H270 Q322 650 338 608 L346 560 Q352 540 380 536 Z" fill="var(--accent)"/>
    </svg>

    <div class="brand">
      <span class="brand-mark"></span>
      <p class="brand-name">K&amp;R Ledger Partners</p>
    </div>
    <p class="email">yusuf.halabi@krledgerpartners.example</p>

    <div class="name-banner">
      <p class="person-name">Yusuf K. Halabi</p>
      <p class="person-title">Senior Financial Consultant</p>
    </div>

    <ul class="contact-list">
      <li>
        <span class="contact-icon">
          <svg width="12" height="12" viewBox="0 0 24 24"><path d="M6.6 10.8a15 15 0 0 0 6.6 6.6l2.2-2.2c.3-.3.7-.4 1-.2 1.1.4 2.3.6 3.6.6.6 0 1 .4 1 1V20c0 .6-.4 1-1 1A17 17 0 0 1 3 4c0-.6.4-1 1-1h3.5c.6 0 1 .4 1 1 0 1.3.2 2.5.6 3.6.1.3 0 .7-.2 1z" fill="#fff"/></svg>
        </span>966-50711-2938
      </li>
      <li>
        <span class="contact-icon">
          <svg width="12" height="12" viewBox="0 0 24 24"><path d="M3 11 12 3l9 8h-3v9h-5v-6h-2v6H6v-9z" fill="#fff"/></svg>
        </span>P.O Box 274816,
      </li>
      <li>
        <span class="contact-icon" style="background:transparent"></span>Jeddah 21947, KSA
      </li>
      <li>
        <span class="contact-icon">
          <svg width="12" height="12" viewBox="0 0 24 24"><path d="M12 2a7 7 0 0 0-7 7c0 5 7 13 7 13s7-8 7-13a7 7 0 0 0-7-7zm0 9.5A2.5 2.5 0 1 1 12 6.5a2.5 2.5 0 0 1 0 5z" fill="#fff"/></svg>
        </span>Jeddah , KSA
      </li>
    </ul>
  </section>

  <section class="card card-back" aria-label="Business card back">
    <svg class="card-shapes" viewBox="0 0 380 660" width="380" height="660" aria-hidden="true">
      <path d="M380 0 H290 Q332 8 344 48 L346 120 Q352 140 380 146 Z" fill="var(--accent)"/>
      <path d="M0 290 Q28 296 32 318 L32 460 Q28 484 0 490 Z" fill="var(--accent-deep)"/>
      <path d="M0 660 H110 Q56 652 40 610 L36 560 Q30 540 0 536 Z" fill="var(--accent)"/>
    </svg>

    <div class="brand">
      <span class="brand-mark"></span>
      <p class="brand-name">K&amp;R Ledger Partners</p>
    </div>

    <div class="signature" role="img" aria-label="Handwritten signature of Yusuf K. Halabi with his title beneath"></div>
  </section>

</body>
</html>
```